'Tarovin' a financial/crypto-currency exchange in the middle east

On the card we need 1) Name 2) title 3) email address 4) phone number using the same colors and theme as the logo. On one side we just want the logo and we want the whole card to be in blue (same blue as logo) with the logo in the back being white.
Industry/Entity Type
Financial

```html
<!DOCTYPE html>
<html lang="en">
<head>
<meta charset="utf-8">
<title>Tarovin – Business Card</title>
<link rel="stylesheet" href="https://fonts.googleapis.com/css2?family=Questrial&family=PT+Sans:ital@0;1&display=swap">
<style>
  :root {
    --brand-blue: #0a8fcb;
    --card-white: #fbfbfb;
    --stage: #e9e8e8;
    --mark-grey: #e4e2e2;
    --mark-grey-light: #efeeee;
    --ink-white: #ffffff;
  }
  * { box-sizing: border-box; margin: 0; padding: 0; }
  html, body {
    width: 1200px; height: 900px; overflow: hidden;
    background: var(--stage);
  }
  .card {
    position: absolute; left: 250px;
    width: 700px; height: 400px;
    border-radius: 30px; overflow: hidden;
    box-shadow: 0 6px 18px rgba(0,0,0,0.12);
  }

  /* Back side: all blue, name in white */
  .card-back { top: 40px; background: var(--brand-blue); }
  .back-rule-lead {
    position: absolute; left: 0; top: 178px;
    width: 300px; height: 3px; background: var(--ink-white);
  }
  .back-seal {
    position: absolute; left: 300px; top: 134px;
    width: 90px; height: 90px; border-radius: 50%;
    border: 6px solid var(--ink-white);
  }
  .back-name-row {
    position: absolute; left: 404px; right: 0; top: 190px;
    display: flex; align-items: flex-end; gap: 10px;
  }
  .back-name-row .brand-name {
    flex: none;
    font-family: "Questrial", sans-serif;
    font-size: 62px; line-height: 1; color: var(--ink-white);
    letter-spacing: 1px;
  }
  .back-name-row .rule-tail {
    flex: 1; min-width: 20px; height: 3px;
    background: var(--ink-white); margin-bottom: 12px;
  }

  /* Front side: contact details */
  .card-front { top: 470px; background: var(--card-white); }
  .contact {
    position: absolute; left: 56px; top: 34px;
    font-family: "PT Sans", sans-serif; color: var(--brand-blue);
  }
  .contact .person-name { font-size: 30px; line-height: 1.1; }
  .contact .job-title { font-size: 18px; margin-left: 2px; }
  .contact .divider {
    width: 76px; height: 3px; background: var(--brand-blue);
    margin: 28px 0;
  }
  .contact .line {
    display: flex; align-items: center; gap: 8px;
    font-size: 19px; margin: 6px 0;
  }
  .contact .line svg { width: 18px; height: 18px; fill: var(--brand-blue); }
  .website {
    position: absolute; left: 56px; bottom: 34px;
    display: flex; align-items: center; gap: 8px;
    font-family: "PT Sans", sans-serif; font-size: 19px; color: var(--brand-blue);
  }
  .website svg { width: 18px; height: 18px; }

  .backdrop-disc {
    position: absolute; left: 360px; top: 50px;
    width: 300px; height: 300px; border-radius: 50%;
    background: var(--mark-grey);
    box-shadow: 0 0 0 12px var(--mark-grey-light), 0 0 0 17px var(--mark-grey);
  }
  .front-lockup {
    position: absolute; left: 336px; top: 152px;
    display: flex; align-items: center; gap: 12px;
  }
  .front-lockup .seal {
    width: 76px; height: 76px; border-radius: 50%;
    background: var(--brand-blue);
  }
  .front-lockup .brand-name {
    font-family: "Questrial", sans-serif;
    font-size: 54px; line-height: 1; color: var(--brand-blue);
    transform: translateY(24px);
  }
</style>
</head>
<body>

  <section class="card card-back" aria-label="Card back">
    <span class="back-rule-lead"></span>
    <span class="back-seal"></span>
    <div class="back-name-row">
      <span class="brand-name">Tarovin</span>
      <span class="rule-tail"></span>
    </div>
  </section>

  <section class="card card-front" aria-label="Card front">
    <div class="backdrop-disc"></div>

    <div class="contact">
      <p class="person-name">Your Name</p>
      <p class="job-title">Job Title</p>
      <div class="divider"></div>
      <p class="line">
        <svg viewBox="0 0 24 24" aria-hidden="true"><path d="M3 8c0-2 3-4 9-4s9 2 9 4v2h-5V8H8v2H3zM6 11h12l2 9H4z"/></svg>
        000 000 0000
      </p>
      <p class="line">
        <svg viewBox="0 0 24 24" aria-hidden="true"><path d="M2 5h20v14H2z M3 6l9 7 9-7" fill="var(--brand-blue)" stroke="#fff" stroke-width="1.5"/></svg>
        youremail@xyz.com
      </p>
      <div class="divider"></div>
    </div>

    <p class="website">
      <svg viewBox="0 0 24 24" aria-hidden="true" fill="none" stroke="var(--brand-blue)" stroke-width="1.6">
        <circle cx="12" cy="12" r="9"/><ellipse cx="12" cy="12" rx="4" ry="9"/><path d="M3 12h18M5 7h14M5 17h14"/>
      </svg>
      www.yourwebsite.com
    </p>

    <div class="front-lockup">
      <span class="seal"></span>
      <span class="brand-name">Tarovin</span>
    </div>
  </section>

</body>
</html>
```